New design for 4 homepage screens (no full design) --> Follow-up business for winner

- Please make sure to read these instructions and the PowerPoint File attached
- Varnoki.com is a Swiss-based online store selling business shirts and accessories for business men
- Please visit the page to make yourself familiar with the company. Although the text is in German, with Google translator you should be able to understand the main content.
- Our clients are mainly business men between 30 and 60 years old. Mostly with a high income working in the service industry (banking, insurance, lawyers, etc.). Sometimes there wives purchase the shirts for them ;-)
- The store is based on Crateloom, so you cannot change the layout freely
- The colors and the logo are given, as they are also used for the print materials (please see files in attachment)
- I am running several business and often need a talented web designer --> the winner gets substantial follow-up business

- Your tasks:
- Please design the four screens you can use in the carousel on the homepage
- The design we use today did not receive good enough feedback
- You are free to use graphic elements or (stock) photos (real or Photoshoped). If you are using photos, they must be properly licensed. If license cost are above US$ 100 please check with me in advance.
- Please make sure the text is not too boring, it is OK, if it is a bit hard to read, not all words same size, different alignment or something like this.
- In the attached file, you can find the text that needs to be on the screens. You do not need to use bullet points or stick to the colors, they are just for illustration purposes.
- The Englisch translation on the right-hand side, is just for you – please use the German texts in you design proposals
- At the end of the day, the conversion is key – so first you need to make sure visitors don’t just jump off the page after their first impression and that they browse to the shop. You can use links to connect with other pages (see current version)

Target Market(s)

Men's business shirts and accessoiries

Industry/Entity Type

Business

Number of Pages Required

4 page

Font styles to use
Other font styles liked:
• Presto

Requirements
Must have
• - Match to the existing logo and colors
• - Fit with target audience (business men 30-60 years old)
Nice to have
• Fits with the key terms of our brand:
• - Successful in your job
• - Performance oriented
• - Fast, simple, easy

```html
<!DOCTYPE html>
<html lang="de">
<head>
<meta charset="utf-8">
<title>Varnoki – Das perfekte Hemd für jeden</title>
<link rel="stylesheet" href="https://fonts.googleapis.com/css2?family=Lato:wght@400;700;900&display=swap">
<style>
:root{
  --ink:#1b1b1d;
  --ink-soft:#2a2a2d;
  --gold:#c9a24a;
  --paper:#ffffff;
  --mist:#f4f4f4;
  --line:#e2e2e2;
  --text:#444;
  --muted:#8a8a8a;
  --price:#e4e4e4;
}
*{box-sizing:border-box;margin:0;padding:0}
html,body{width:1200px;height:2748px;overflow:hidden}
body{font-family:"Lato",Arial,sans-serif;color:var(--text);background:var(--paper);position:relative}

.topbar{height:32px;background:var(--ink);color:#cfcfcf;font-size:11px;display:flex;align-items:center;justify-content:space-between;padding:0 40px}
.topbar .promo{color:var(--gold)}
.topbar .cart{display:flex;gap:8px;align-items:center}
.cart-count{background:var(--gold);color:var(--ink);font-weight:700;padding:1px 5px;border-radius:2px}

.masthead{height:128px;display:flex;flex-direction:column;align-items:center;justify-content:center;gap:6px}
.brand-mark{width:26px;height:26px;background:var(--gold)}
.brand-name{font-size:34px;font-weight:900;letter-spacing:8px;color:var(--gold)}

.mainnav{height:24px;background:var(--ink);display:flex;justify-content:center;gap:36px;align-items:center}
.mainnav a{color:#e6e6e6;font-size:10px;font-weight:700;letter-spacing:1px;text-decoration:none}

.hero{position:relative;height:488px;overflow:hidden}
.hero-photo{position:absolute;inset:0;background:
  radial-gradient(ellipse 170px 200px at 760px 330px,rgba(30,30,34,.95),rgba(30,30,34,0) 100%),
  radial-gradient(ellipse 260px 220px at 800px 430px,rgba(25,25,28,.9),rgba(25,25,28,0) 100%),
  radial-gradient(ellipse 110px 120px at 735px 150px,rgba(196,160,130,.85),rgba(196,160,130,0) 100%),
  radial-gradient(ellipse 330px 210px at 520px 380px,rgba(210,214,218,.85),rgba(210,214,218,0) 100%),
  radial-gradient(ellipse 260px 320px at 1080px 250px,rgba(60,56,52,.8),rgba(60,56,52,0) 100%),
  linear-gradient(100deg,#2e2d2b 0%,#57534e 22%,#9c968d 45%,#c9c4bb 62%,#8b857c 82%,#4a4641 100%)}
.hero-copy{position:absolute;left:200px;top:48px;color:#fff}
.hero-title{font-size:42px;font-weight:700;line-height:1.12;text-shadow:0 2px 6px rgba(0,0,0,.45)}
.hero-sub{display:inline-block;margin-top:12px;font-size:16px;border:1px solid rgba(255,255,255,.85);padding:4px 10px;background:rgba(0,0,0,.3)}
.hero-arrow{position:absolute;top:200px;width:40px;height:84px;background:rgba(255,255,255,.55);display:flex;align-items:center;justify-content:center}
.hero-arrow.prev{left:0}.hero-arrow.next{right:0}

.catalog{padding-top:44px}
.category{height:432px}
.category-title{height:40px;display:flex;align-items:center;justify-content:center;gap:18px;font-size:19px;font-weight:700;letter-spacing:2px;color:var(--ink)}
.category-title::before,.category-title::after{content:"";width:300px;height:2px;background:var(--gold)}
.carousel{margin-top:28px;position:relative;height:340px}
.carousel-arrow{position:absolute;top:88px}
.carousel-arrow.prev{left:108px}.carousel-arrow.next{right:108px}
.products{display:flex;gap:36px;justify-content:center}
.product{width:200px;height:340px;display:flex;flex-direction:column}
.product-photo{height:200px;border:1px solid var(--line);background-color:var(--paper)}
.product-tag{height:26px;background:var(--ink-soft);color:#fff;font-size:11px;font-weight:700;display:flex;align-items:center;justify-content:center;margin-top:8px}
.product-name{flex:1;font-size:11px;line-height:1.45;text-align:center;padding:8px 10px 0;color:var(--text)}
.product-price{height:28px;background:var(--price);font-size:11px;display:flex;align-items:center;justify-content:center;gap:6px;color:var(--ink)}
.product-price s{color:var(--muted)}

.shirt-white{background-image:radial-gradient(ellipse 62px 82px at 50% 52%,#e4e6ea 0%,#eef0f2 60%,rgba(255,255,255,0) 100%)}
.shirt-lilac{background-image:radial-gradient(ellipse 62px 82px at 50% 52%,#d6d4e4 0%,#e6e5ef 60%,rgba(255,255,255,0) 100%)}
.shirt-blue{background-image:radial-gradient(ellipse 62px 82px at 50% 52%,#bccde6 0%,#d7e1f0 60%,rgba(255,255,255,0) 100%)}
.tie-red{background-image:radial-gradient(ellipse 22px 82px at 50% 50%,#6b1c28 0%,#7d2633 55%,rgba(255,255,255,0) 100%)}
.square-red{background-image:radial-gradient(ellipse 58px 58px at 50% 50%,#5a1a22 0%,#6e2530 60%,rgba(255,255,255,0) 100%)}
.tie-blue{background-image:radial-gradient(ellipse 22px 82px at 50% 50%,#1f3fc0 0%,#2f55d6 55%,rgba(255,255,255,0) 100%)}
.cufflink{background-image:radial-gradient(ellipse 70px 30px at 50% 52%,#a9abb0 0%,#cfd0d4 55%,rgba(255,255,255,0) 100%)}
.cufflink-red{background-image:radial-gradient(ellipse 70px 30px at 50% 52%,#8a2a44 0%,#b9a3ab 60%,rgba(255,255,255,0) 100%)}
.cufflink-white{background-image:radial-gradient(ellipse 70px 30px at 50% 52%,#d9d9dc 0%,#ececee 55%,rgba(255,255,255,0) 100%)}
.belt-brown{background-image:radial-gradient(ellipse 80px 40px at 50% 52%,#6d3f1f 0%,#8c5530 55%,rgba(255,255,255,0) 100%)}
.belt-black{background-image:radial-gradient(ellipse 80px 40px at 50% 52%,#141416 0%,#2e2e31 55%,rgba(255,255,255,0) 100%)}

.site-footer{position:absolute;left:0;top:2460px;width:1200px;height:288px;background:var(--ink);color:#bdbdbd}
.footer-cols{display:flex;padding:36px 90px 0 180px;gap:60px;height:240px}
.footer-col{flex:1}
.footer-col h3{color:var(--gold);font-size:13px;font-weight:700;letter-spacing:1px;margin-bottom:14px}
.footer-col ul{list-style:none;font-size:11px;line-height:2}
.footer-col p{font-size:11px;line-height:1.7}
.follow{margin-top:18px}
.follow-icons{display:flex;gap:8px}
.follow-icons span{width:20px;height:20px;background:#555}
.signup{display:flex;margin-top:12px}
.signup-field{flex:1;height:28px;background:#fff}
.signup-btn{width:70px;height:28px;background:var(--gold);color:var(--ink);font-size:11px;font-weight:700;display:flex;align-items:center;justify-content:center}
.contact-line{display:flex;align-items:center;gap:8px;font-size:11px;margin-bottom:8px}
.footer-bottom{height:48px;border-top:1px solid #333;display:flex;align-items:center;justify-content:space-between;padding:0 40px;font-size:10px;color:#888}
.to-top{width:24px;height:24px;border-radius:50%;background:#3a3a3d;display:flex;align-items:center;justify-content:center}
</style>
</head>
<body>

<div class="topbar">
  <span>Ihr Konto ▾</span>
  <span class="promo">Kostenloser Versand | 30 Tage Rückgaberecht</span>
  <span class="cart">Warenkorb <span class="cart-count">0</span></span>
</div>

<header class="masthead">
  <span class="brand-mark"></span>
  <span class="brand-name">VARNOKI</span>
</header>

<nav class="mainnav">
  <a href="#">HOME</a><a href="#">ÜBER UNS</a><a href="#">HEMDEN</a><a href="#">ZUBEHÖR</a><a href="#">GÜRTEL</a><a href="#">FAQ</a><a href="#">KONTAKT</a>
</nav>

<section class="hero">
  <div class="hero-photo" role="img" aria-label="Foto: Geschäftsmann in weissem Hemd, Krawatte und dunkler Weste sitzt auf einem hellen Sofa"></div>
  <div class="hero-copy">
    <h1 class="hero-title">Das perfekte<br>Hemd für jeden</h1>
    <span class="hero-sub">Bequem | Einfach | Garantierte Qualität</span>
  </div>
  <div class="hero-arrow prev"><svg width="14" height="24"><path d="M12 2 2 12l10 10" fill="none" stroke="#fff" stroke-width="3"/></svg></div>
  <div class="hero-arrow next"><svg width="14" height="24"><path d="M2 2l10 10L2 22" fill="none" stroke="#fff" stroke-width="3"/></svg></div>
</section>

<main class="catalog">

  <section class="category">
    <h2 class="category-title">HEMDEN</h2>
    <div class="carousel">
      <svg class="carousel-arrow prev" width="12" height="22"><path d="M10 2 2 11l8 9" fill="none" stroke="#999" stroke-width="2"/></svg>
      <svg class="carousel-arrow next" width="12" height="22"><path d="M2 2l8 9-8 9" fill="none" stroke="#999" stroke-width="2"/></svg>
      <div class="products">
        <article class="product"><div class="product-photo shirt-lilac" role="img" aria-label="Foto: gefaltetes fliederfarbenes Businesshemd"></div><div class="product-tag">Varnoki – Aktuell "Office"</div><p class="product-name">Fliederfarbenes Hemd<br>Slim Fit (Grösse 38–46)</p><div class="product-price"><s>CHF 99.00</s> CHF 79.00</div></article>
        <article class="product"><div class="product-photo shirt-blue" role="img" aria-label="Foto: gefaltetes hellblaues Businesshemd"></div><div class="product-tag">Varnoki – Aktuell "Office"</div><p class="product-name">Hellblaues Businesshemd<br>Regular Fit (Grösse 38–46)</p><div class="product-price"><s>CHF 99.00</s> CHF 79.00</div></article>
        <article class="product"><div class="product-photo shirt-blue" role="img" aria-label="Foto: gefaltetes blaues Businesshemd"></div><div class="product-tag">Varnoki – Aktuell "Office"</div><p class="product-name">Blaues Businesshemd<br>Mit Kentkragen (38–46)</p><div class="product-price"><s>CHF 99.00</s> CHF 79.00</div></article>
        <article class="product"><div class="product-photo shirt-white" role="img" aria-label="Foto: gefaltetes weisses Hemd"></div><div class="product-tag">Varnoki – Aktuell "Office"</div><p class="product-name">Weisses Hemd mit Struktur<br>Tailored Fit (38–46)</p><div class="product-price"><s>CHF 99.00</s> CHF 79.00</div></article>
      </div>
    </div>
  </section>

  <section class="category">
    <h2 class="category-title">KRAWATTEN &amp; EINSTECKTÜCHER</h2>
    <div class="carousel">
      <svg class="carousel-arrow prev" width="12" height="22"><path d="M10 2 2 11l8 9" fill="none" stroke="#999" stroke-width="2"/></svg>
      <svg class="carousel-arrow next" width="12" height="22"><path d="M2 2l8 9-8 9" fill="none" stroke="#999" stroke-width="2"/></svg>
      <div class="products">
        <article class="product"><div class="product-photo tie-red" role="img" aria-label="Foto: bordeauxrote Krawatte"></div><div class="product-tag">Promo</div><p class="product-name">Bordeauxrote Krawatte<br>aus reiner Seide</p><div class="product-price">CHF 79.00</div></article>
        <article class="product"><div class="product-photo tie-red" role="img" aria-label="Foto: rote Strickkrawatte"></div><div class="product-tag">Promo</div><p class="product-name">Rote Strickkrawatte<br>schmal geschnitten</p><div class="product-price">CHF 79.00</div></article>
        <article class="product"><div class="product-photo square-red" role="img" aria-label="Foto: gemustertes Einstecktuch"></div><div class="product-tag">Promo</div><p class="product-name">Gemustertes Einstecktuch<br>in Bordeaux</p><div class="product-price">CHF 49.00</div></article>
        <article class="product"><div class="product-photo tie-blue" role="img" aria-label="Foto: königsblaue Krawatte"></div><div class="product-tag">Promo</div><p class="product-name">Königsblaue Krawatte<br>aus reiner Seide</p><div class="product-price">CHF 79.00</div></article>
      </div>
    </div>
  </section>

  <section class="category">
    <h2 class="category-title">MANSCHETTENKNÖPFE</h2>
    <div class="carousel">
      <svg class="carousel-arrow prev" width="12" height="22"><path d="M10 2 2 11l8 9" fill="none" stroke="#999" stroke-width="2"/></svg>
      <svg class="carousel-arrow next" width="12" height="22"><path d="M2 2l8 9-8 9" fill="none" stroke="#999" stroke-width="2"/></svg>
      <div class="products">
        <article class="product"><div class="product-photo cufflink" role="img" aria-label="Foto: silberne Manschettenknöpfe"></div><div class="product-tag">Promo</div><p class="product-name">Silberne Manschettenknöpfe<br>mit Gravur, poliert</p><div class="product-price">CHF 69.00</div></article>
        <article class="product"><div class="product-photo cufflink-red" role="img" aria-label="Foto: Manschettenknöpfe mit roter Einlage"></div><div class="product-tag">Promo</div><p class="product-name">Manschettenknöpfe mit<br>roter Einlage, rund</p><div class="product-price">CHF 69.00</div></article>
        <article class="product"><div class="product-photo cufflink-white" role="img" aria-label="Foto: weisse Manschettenknöpfe"></div><div class="product-tag">Promo</div><p class="product-name">Weisse Manschettenknöpfe<br>mit Perlmutt</p><div class="product-price">CHF 69.00</div></article>
        <article class="product"><div class="product-photo cufflink-red" role="img" aria-label="Foto: Manschettenknöpfe in Bordeaux"></div><div class="product-tag">Promo</div><p class="product-name">Manschettenknöpfe in<br>Bordeaux, eckig</p><div class="product-price">CHF 69.00</div></article>
      </div>
    </div>
  </section>

  <section class="category">
    <h2 class="category-title">GÜRTEL</h2>
    <div class="carousel">
      <svg class="carousel-arrow prev" width="12" height="22"><path d="M10 2 2 11l8 9" fill="none" stroke="#999" stroke-width="2"/></svg>
      <svg class="carousel-arrow next" width="12" height="22"><path d="M2 2l8 9-8 9" fill="none" stroke="#999" stroke-width="2"/></svg>
      <div class="products">
        <article class="product"><div class="product-photo belt-brown" role="img" aria-label="Foto: aufgerollter brauner Ledergürtel"></div><div class="product-tag">Promo</div><p class="product-name">Brauner Ledergürtel<br>mit silberner Schnalle</p><div class="product-price">CHF 89.00</div></article>
        <article class="product"><div class="product-photo belt-brown" role="img" aria-label="Foto: aufgerollter dunkelbrauner Ledergürtel"></div><div class="product-tag">Promo</div><p class="product-name">Dunkelbrauner Gürtel<br>aus Vollleder</p><div class="product-price">CHF 89.00</div></article>
        <article class="product"><div class="product-photo belt-black" role="img" aria-label="Foto: aufgerollter schwarzer Ledergürtel"></div><div class="product-tag">Promo</div><p class="product-name">Schwarzer Ledergürtel<br>klassisch, glatt</p><div class="product-price">CHF 89.00</div></article>
        <article class="product"><div class="product-photo belt-black" role="img" aria-label="Foto: schwarzer Gürtel mit matter Schnalle"></div><div class="product-tag">Promo</div><p class="product-name">Schwarzer Gürtel mit<br>matter Schnalle</p><div class="product-price">CHF 89.00</div></article>
      </div>
    </div>
  </section>

</main>

<footer class="site-footer">
  <div class="footer-cols">
    <div class="footer-col">
      <h3>NAVIGATION</h3>
      <ul><li>Suche</li><li>Über uns</li><li>AGB</li></ul>
      <div class="follow">
        <h3>Folge uns</h3>
        <div class="follow-icons"><span></span><span></span></div>
      </div>
    </div>
    <div class="footer-col">
      <h3>In Verbindung Bleiben</h3>
      <p>Abonnieren Sie unseren Newsletter und erhalten Sie exklusive Angebote.</p>
      <div class="signup"><div class="signup-field"></div><div class="signup-btn">Senden</div></div>
    </div>
    <div class="footer-col">
      <h3>Kontaktiere Uns</h3>
      <div class="contact-line"><svg width="12" height="14"><path d="M6 1a4.5 4.5 0 0 0-4.5 4.5C1.5 9 6 13 6 13s4.5-4 4.5-7.5A4.5 4.5 0 0 0 6 1z" fill="var(--gold)"/></svg>Varnoki GmbH, Musterweg 12, 8001 Zürich</div>
      <div class="contact-line"><svg width="12" height="12"><path d="M2 1h3l1 3-2 1a7 7 0 0 0 3 3l1-2 3 1v3c-6 0-9-3-9-9z" fill="var(--gold)"/></svg>+41 44 000 00 00</div>
      <div class="contact-line"><svg width="12" height="10"><rect x=".5" y=".5" width="11" height="9" fill="none" stroke="var(--gold)"/><path d="M1 1l5 4 5-4" fill="none" stroke="var(--gold)"/></svg>info@varnoki.com</div>
    </div>
  </div>
  <div class="footer-bottom">
    <span>Copyright © 2024 Varnoki.com. Powered by Crateloom</span>
    <span class="to-top"><svg width="10" height="8"><path d="M1 7l4-5 4 5" fill="none" stroke="#ccc" stroke-width="1.6"/></svg></span>
  </div>
</footer>

</body>
</html>
```